Wedding Photography business card

I need a business card made for a wedding photography business. Formal, unique, i like dark colors maybe black, white, gray, deep blue, silver. Sharp.

This is an idea i have i don't know if it would work.
Think Palm Beach, florida

work in mirror mode in your design program, Just an idea

Front side:
feminine, classy maybe white from wedding dress,
script, elegant,

back side:
masculine, black from tux, symbolizing strength, power,
serif

RV Photography
(555) 214-3097
www.ruthvlenses.example

Target Market(s)

upscale Weddings, targeting bride and groom

Industry/Entity Type

Wedding

Font styles to use
Serif
Script

Colors

Designer to choose colors to be used in the design.

Requirements
Must have
• both sides match somehow

```html
<!DOCTYPE html>
<html lang="en">
<head>
<meta charset="utf-8">
<title>RV Photography – Business Card</title>
<link rel="stylesheet" href="https://fonts.googleapis.com/css2?family=EB+Garamond:wght@400&family=Pinyon+Script&display=swap">
<style>
  :root {
    --backdrop: #666666;
    --paper: #ffffff;
    --ink: #000000;
    --ink-reverse: #ffffff;
    --tone-soft: #d9d9d9;
  }
  * { margin: 0; padding: 0; box-sizing: border-box; }
  html, body {
    width: 1200px;
    height: 1000px;
    overflow: hidden;
    background: var(--backdrop);
  }
  .canvas {
    position: relative;
    width: 1200px;
    height: 1000px;
    font-family: "EB Garamond", Georgia, serif;
  }
  .card {
    position: absolute;
    top: 169px;
    width: 367px;
    height: 661px;
    background: var(--paper);
    overflow: hidden;
  }
  .card--front { left: 93px; }
  .card--back { left: 741px; height: 660px; }

  /* Area reserved for the groom's tie artwork */
  .tie-art {
    position: absolute;
    left: 119px;
    top: 0;
    width: 129px;
    height: 661px;
    background: var(--ink);
  }

  /* Area reserved for the bride's gown silhouette artwork */
  .gown-art {
    position: absolute;
    left: 0;
    top: 0;
    width: 100%;
    height: 445px;
    background: linear-gradient(180deg, var(--ink) 0%, var(--tone-soft) 55%, var(--paper) 100%);
  }

  .tie-label {
    position: absolute;
    left: 119px;
    width: 129px;
    text-align: center;
    color: var(--ink-reverse);
    line-height: 1;
  }
  .tie-label__name {
    top: 544px;
    font-family: "Pinyon Script", cursive;
    font-size: 23px;
  }
  .tie-label__trade {
    top: 575px;
    font-size: 14px;
    letter-spacing: 1.6px;
  }

  .contact {
    position: absolute;
    left: 0;
    top: 503px;
    width: 100%;
    text-align: center;
    color: var(--ink);
    line-height: 1;
  }
  .contact__name {
    font-family: "Pinyon Script", cursive;
    font-size: 24px;
  }
  .contact__trade {
    margin-top: 3px;
    font-size: 17px;
    letter-spacing: 0.6px;
  }
  .contact__phone {
    margin-top: 8px;
    font-size: 14px;
    letter-spacing: 0.4px;
  }
  .contact__web {
    margin-top: 8px;
    font-size: 13.5px;
    letter-spacing: 0.6px;
  }
</style>
</head>
<body>
<main class="canvas">

  <section class="card card--front" aria-label="Business card front">
    <div class="tie-art" role="img" aria-label="Black necktie illustration running down the card"></div>
    <p class="tie-label tie-label__name">Ruth Vance</p>
    <p class="tie-label tie-label__trade">photography</p>
  </section>

  <section class="card card--back" aria-label="Business card back">
    <div class="gown-art" role="img" aria-label="Black and white silhouette of a wedding gown bodice"></div>
    <div class="contact">
      <p class="contact__name">Ruth Vance</p>
      <p class="contact__trade">wedding photography</p>
      <p class="contact__phone">(555) 214-3097</p>
      <p class="contact__web">www.ruthvlenses.example</p>
    </div>
  </section>

</main>
</body>
</html>
```